NEW YORK Plumbing/utility company 10 year anniversary business card

Looking For simple back and front business card would like to include a few things in description
We offer 24/7 emergency service
residential
commercial
industrial
municipal
services offered
Plumbing
hydro excavation
hydro jetting
Well pumps
Sewer pumps
water mains
sewer mains

```html
<!DOCTYPE html>
<html lang="en">
<head>
<meta charset="utf-8">
<title>Ridgeline Water &amp; Sewer – Business Card</title>
<link rel="stylesheet" href="https://fonts.googleapis.com/css2?family=Montserrat:wght@400;500;700;800&display=swap">
<style>
  :root {
    --stage: #2b2b2d;
    --sky: #35a9e2;
    --sky-deep: #2b93d0;
    --navy: #1f68ad;
    --band: #1d6cb3;
    --ink: #3d3d3d;
    --white: #ffffff;
  }
  * { box-sizing: border-box; margin: 0; padding: 0; }
  html, body { width: 1200px; height: 1186px; overflow: hidden; }
  body {
    background: var(--stage);
    font-family: "Montserrat", sans-serif;
    display: flex;
    flex-direction: column;
    align-items: center;
    justify-content: center;
    gap: 64px;
  }
  .card {
    position: relative;
    width: 900px;
    height: 514px;
    border-radius: 28px;
    overflow: hidden;
  }

  /* Back side */
  .card--back {
    background: linear-gradient(100deg, var(--sky-deep) 0%, var(--sky) 55%, #3cb1e8 100%);
    color: var(--white);
  }
  .card--back .brand {
    position: absolute;
    left: 0; right: 0; top: 110px;
    text-align: center;
  }
  .brand-name {
    font-weight: 800;
    font-size: 68px;
    letter-spacing: 2px;
    line-height: 1;
  }
  .brand-sub {
    margin-top: 18px;
    display: flex;
    align-items: center;
    justify-content: center;
    gap: 18px;
    font-weight: 800;
    font-size: 34px;
    letter-spacing: 4px;
  }
  .brand-sub .rule { width: 90px; height: 3px; background: currentColor; }
  .services {
    position: absolute;
    left: 80px; right: 80px; top: 340px;
    list-style: none;
    display: flex;
    flex-wrap: wrap;
    justify-content: center;
    gap: 22px 34px;
    font-size: 21px;
    font-weight: 400;
  }
  .services li { display: flex; align-items: center; gap: 10px; }
  .services svg { width: 24px; height: 24px; flex: none; }

  /* Front side */
  .card--front { background: var(--white); }
  .card--front .brand {
    position: absolute;
    left: 70px; top: 70px;
    color: var(--navy);
  }
  .card--front .brand-name { font-size: 60px; }
  .card--front .brand-sub { justify-content: flex-start; font-size: 30px; color: var(--sky-deep); }
  .contact-block {
    position: absolute;
    left: 70px; top: 270px;
    display: flex;
    align-items: center;
    gap: 28px;
  }
  .person-name { font-size: 38px; font-weight: 700; color: var(--navy); }
  .person-title { font-size: 22px; font-weight: 500; color: var(--ink); margin-top: 2px; }
  .divider { width: 2px; height: 74px; background: var(--navy); }
  .contact-list { list-style: none; font-size: 21px; color: var(--ink); }
  .contact-list li { display: flex; align-items: center; gap: 12px; line-height: 1.55; }
  .contact-list svg { width: 20px; height: 20px; fill: var(--navy); }
  .sectors {
    position: absolute;
    left: 0; right: 0; bottom: 38px;
    height: 76px;
    background: var(--band);
    display: flex;
    align-items: center;
    justify-content: space-around;
    padding: 0 40px;
    list-style: none;
    color: var(--white);
    font-size: 21px;
    font-weight: 700;
    letter-spacing: 0.5px;
  }
  .sectors li::before {
    content: "";
    display: inline-block;
    width: 9px; height: 9px;
    border-radius: 50%;
    background: var(--white);
    margin-right: 10px;
    vertical-align: middle;
  }
</style>
</head>
<body>

<section class="card card--back" aria-label="Card back">
  <div class="brand">
    <div class="brand-name">RIDGELINE</div>
    <div class="brand-sub"><span class="rule"></span>WATER &amp; SEWER<span class="rule"></span></div>
  </div>
  <ul class="services">
    <li><svg viewBox="0 0 24 24"><circle cx="12" cy="12" r="11" fill="#fff"/><path d="M7 7l10 10M17 7L7 17" stroke="#2b93d0" stroke-width="2.4" stroke-linecap="round"/></svg>Plumbing</li>
    <li><svg viewBox="0 0 24 24"><circle cx="12" cy="12" r="11" fill="#fff"/><path d="M7 7l10 10M17 7L7 17" stroke="#2b93d0" stroke-width="2.4" stroke-linecap="round"/></svg>Hydro excavation</li>
    <li><svg viewBox="0 0 24 24"><circle cx="12" cy="12" r="11" fill="#fff"/><path d="M7 7l10 10M17 7L7 17" stroke="#2b93d0" stroke-width="2.4" stroke-linecap="round"/></svg>Hydro jetting</li>
    <li><svg viewBox="0 0 24 24"><circle cx="12" cy="12" r="11" fill="#fff"/><path d="M7 7l10 10M17 7L7 17" stroke="#2b93d0" stroke-width="2.4" stroke-linecap="round"/></svg>Well pumps</li>
    <li><svg viewBox="0 0 24 24"><circle cx="12" cy="12" r="11" fill="#fff"/><path d="M7 7l10 10M17 7L7 17" stroke="#2b93d0" stroke-width="2.4" stroke-linecap="round"/></svg>Sewer pumps</li>
    <li><svg viewBox="0 0 24 24"><circle cx="12" cy="12" r="11" fill="#fff"/><path d="M7 7l10 10M17 7L7 17" stroke="#2b93d0" stroke-width="2.4" stroke-linecap="round"/></svg>Water mains</li>
    <li><svg viewBox="0 0 24 24"><circle cx="12" cy="12" r="11" fill="#fff"/><path d="M7 7l10 10M17 7L7 17" stroke="#2b93d0" stroke-width="2.4" stroke-linecap="round"/></svg>Sewer mains</li>
  </ul>
</section>

<section class="card card--front" aria-label="Card front">
  <div class="brand">
    <div class="brand-name">RIDGELINE</div>
    <div class="brand-sub"><span class="rule"></span>WATER &amp; SEWER<span class="rule"></span></div>
  </div>
  <div class="contact-block">
    <div class="person">
      <div class="person-name">Daniel Porter</div>
      <div class="person-title">Managing Director</div>
    </div>
    <div class="divider"></div>
    <ul class="contact-list">
      <li><svg viewBox="0 0 24 24"><path d="M6.6 10.8a15.1 15.1 0 006.6 6.6l2.2-2.2a1 1 0 011-.25 11.4 11.4 0 003.6.57 1 1 0 011 1V20a1 1 0 01-1 1A17 17 0 013 4a1 1 0 011-1h3.5a1 1 0 011 1c0 1.25.2 2.45.57 3.57a1 1 0 01-.25 1z"/></svg>555-014-2280</li>
      <li><svg viewBox="0 0 24 24"><path d="M2 5h20v14H2z" opacity=".0"/><path d="M3 5h18a1 1 0 011 1v.4l-10 6.2L2 6.4V6a1 1 0 011-1zm-1 3.7l10 6.2 10-6.2V18a1 1 0 01-1 1H3a1 1 0 01-1-1z"/></svg>info@ridgelinews.com</li>
    </ul>
  </div>
  <ul class="sectors">
    <li>RESIDENTIAL</li>
    <li>COMMERICAL</li>
    <li>INDUTRIAL</li>
    <li>MUNICIPAL</li>
  </ul>
</section>

</body>
</html>
```